Harborlight Willow Home Care Business Cards

We are looking to create double sided, sleek business cards for our new Home Health Care Agency, Harborlight Willow Home Care, located in NJ. We want to appear established, professional and at the same time, stand out with a creative and original flair. It should have a luxurious, exclusive feel to it.
The theme colors from our logo should be incorporated into the project.

Our Logo is attached.

Information to be included on the business cards:

Insert Phone Icon: (555)-204-7390
Insert Website Icon: hwhcpx.example
Insert E-mail Icon: info@hwhcpx.example

Follow us on Social Media!
Insert Facebook Icon: (I will provide the link at a later time)
Insert Instagram Icon (I will provide the link at a later time)

In regard to location, we service the areas of: Bayville
Beachwood
Brick
Deal
Howell
Island Heights
Jackson
Lakehurst
Lakewood
Manchester Township
Point Pleasant Beach
Roosevelt
Long Branch
Toms River

All all it's neighboring areas.

However, that can take up a lot of room...therefore, I had in mind to use the backside of the card to have a MAP with all these areas marked on there...in addition to listing these service locations below the map.

We want the card to appear lively and vibrant.

Please note: I will provide the potential winner with the contact's name later on in the process.

A sample idea is attached below as well.

Use your creative juices!

Good luck!

• A map of our service areas on the back of the double sided card.
Sleek design
Our logo (refer to attachment below)

```html
<!DOCTYPE html>
<html lang="en">
<head>
<meta charset="utf-8">
<title>Harborlight Willow Home Care – Business Cards</title>
<link rel="stylesheet" href="https://fonts.googleapis.com/css2?family=Montserrat:wght@400;500;600;700&display=swap">
<style>
  :root {
    --navy: #0a4e91;
    --lime: #8cc63f;
    --white: #ffffff;
    --backdrop: #dedede;
  }
  * { margin: 0; padding: 0; box-sizing: border-box; }
  html, body {
    width: 1200px; height: 1200px; overflow: hidden;
    background: var(--backdrop);
    font-family: "Montserrat", sans-serif;
  }
  .card {
    position: absolute; left: 208px; width: 791px; height: 452px;
    border-radius: 26px; overflow: hidden;
  }
  .card--front { top: 112px; background: var(--white); }
  .card--back  { top: 644px; background: var(--navy); }
  .waves { position: absolute; inset: 0; width: 100%; height: 100%; }

  .brand {
    position: absolute; text-align: center;
    font-weight: 700; text-transform: uppercase; letter-spacing: 0.5px;
  }
  .brand__mark {
    display: block; margin: 0 auto 14px; width: 92px; height: 92px;
    border-radius: 50%; border: 5px solid var(--lime);
  }
  .brand__name { font-size: 23px; line-height: 1.25; }
  .card--front .brand { left: 431px; top: 46px; width: 340px; }
  .card--front .brand__name { color: var(--navy); }
  .card--back .brand { left: 40px; top: 110px; width: 370px; }
  .card--back .brand__mark { width: 130px; height: 130px; margin-bottom: 22px; border-width: 6px; }
  .card--back .brand__name { color: var(--white); font-size: 28px; }

  .person { position: absolute; left: 41px; top: 202px; color: var(--white); }
  .person__name { color: var(--lime); font-weight: 700; font-size: 28px; letter-spacing: 1px; text-transform: uppercase; }
  .person__role { font-size: 19px; font-weight: 400; margin-top: 2px; }

  .contacts { position: absolute; left: 41px; list-style: none; color: var(--white); font-size: 20.5px; }
  .contacts li { display: flex; align-items: center; height: 25.5px; }
  .contacts--social { top: 279px; }
  .contacts--direct { top: 343px; }
  .contacts .icon { width: 15px; height: 15px; margin-right: 8px; flex: none; }
  .dot { width: 13px; height: 13px; border-radius: 50%; background: var(--lime); margin-right: 8px; flex: none; }

  .areas { position: absolute; left: 452px; top: 33px; list-style: none; color: var(--white); font-size: 23.5px; }
  .areas li { display: flex; align-items: center; height: 29.6px; }
  .areas li::before {
    content: ""; width: 16px; height: 16px; border-radius: 50%;
    background: var(--lime); margin-right: 14px;
  }
</style>
</head>
<body>

<section class="card card--front">
  <svg class="waves" viewBox="0 0 1265 723" preserveAspectRatio="none" aria-hidden="true">
    <path fill="var(--lime)" d="M0,107 C250,95 500,230 660,355 C820,480 1000,620 1265,588 L1265,602 C1000,645 800,515 650,405 C500,295 250,158 0,160 Z"/>
    <path fill="var(--navy)" d="M0,172 C250,150 480,285 640,405 C800,525 1000,655 1265,614 L1265,723 L0,723 Z"/>
    <path fill="var(--navy)" d="M642,350 C810,455 1010,570 1265,503 L1265,572 C1040,612 840,480 642,350 Z"/>
  </svg>

  <div class="brand">
    <span class="brand__mark"></span>
    <p class="brand__name">Harborlight Willow<br>Home Care</p>
  </div>

  <div class="person">
    <h1 class="person__name">Dana Whitfield</h1>
    <p class="person__role">Director</p>
  </div>

  <ul class="contacts contacts--social">
    <li><span class="dot"></span>@Icon: hwhcpx.example</li>
    <li><span class="dot"></span>/Icon: hwhcpx.example</li>
  </ul>

  <ul class="contacts contacts--direct">
    <li>
      <svg class="icon" viewBox="0 0 24 24" fill="none" stroke="var(--lime)" stroke-width="2" aria-hidden="true"><path d="M5 3h4l2 5-2.5 1.5a11 11 0 0 0 6 6L16 13l5 2v4a2 2 0 0 1-2 2A16 16 0 0 1 3 5a2 2 0 0 1 2-2z"/></svg>
      555-204-7390
    </li>
    <li>
      <svg class="icon" viewBox="0 0 24 24" fill="none" stroke="var(--lime)" stroke-width="2" aria-hidden="true"><rect x="2" y="5" width="20" height="14" rx="1"/><path d="M2 6l10 7 10-7"/></svg>
      Icon: info@hwhcpx.example
    </li>
    <li>
      <svg class="icon" viewBox="0 0 24 24" fill="none" stroke="var(--lime)" stroke-width="1.6" aria-hidden="true"><circle cx="12" cy="12" r="10"/><ellipse cx="12" cy="12" rx="4" ry="10"/><path d="M2 12h20M4 7h16M4 17h16"/></svg>
      www.Icon: hwhcpx.example
    </li>
  </ul>
</section>

<section class="card card--back">
  <div class="brand">
    <span class="brand__mark"></span>
    <p class="brand__name">Harborlight Willow<br>Home Care</p>
  </div>

  <ul class="areas">
    <li>Beachwood</li>
    <li>Brick</li>
    <li>Deal</li>
    <li>Howell</li>
    <li>Island Heights</li>
    <li>Jackson</li>
    <li>Lakehurst</li>
    <li>Lakewood</li>
    <li>Manchester Township</li>
    <li>Point Pleasant Beach</li>
    <li>Roosevelt</li>
    <li>Long Branch</li>
    <li>Toms River</li>
  </ul>
</section>

</body>
</html>
```